Simple and Clean business card design

We would like the design to be simple clean and to incorporate our colors.

We are open to your design and talent, we have the dots in our logo as we think of it as data points and we connect data points for people.

We are open to see the great creative and clean design you bring to the table

Contact Information for Business Card

please include: name, position, email, phone and website

Font styles to use
Sans Serif

Requirements
Must have
• my colors incorporated, simplicity
Nice to have
• lots of white space, simplicity
Should not have
• complexicity/ complex art

```html
<!DOCTYPE html>
<html lang="en">
<head>
<meta charset="utf-8">
<title>Bramble — Business Card</title>
<link rel="stylesheet" href="https://fonts.googleapis.com/css2?family=Montserrat:wght@400;500;700&display=swap">
<style>
  :root {
    --stage: #262627;
    --card-light: #ffffff;
    --card-dark: #1d1d1e;
    --ink: #111111;
    --ink-soft: #7a7a7a;
    --paper-text: #ffffff;
    --url-grey: #8a8a8a;
    --brand-blue: #5479c0;
    --dot-light: #f1f2f4;
    --dot-dark-1: #232324;
    --dot-dark-2: #2e2e2f;
    --dot-dark-3: #353536;
  }
  * { margin: 0; padding: 0; box-sizing: border-box; }
  html, body {
    width: 1200px; height: 909px; overflow: hidden;
    background: var(--stage);
    font-family: "Montserrat", sans-serif;
  }
  .canvas { position: relative; width: 1200px; height: 909px; }

  .card {
    position: absolute; width: 560px; height: 320px;
    border-radius: 3px; overflow: hidden;
    box-shadow: 0 18px 40px rgba(0,0,0,.45);
  }
  .card-front { left: 320px; top: 90px; background: var(--card-light); }
  .card-back  { left: 320px; top: 500px; background: var(--card-dark); }

  .decor { position: absolute; inset: 0; width: 100%; height: 100%; }

  .wordmark {
    position: absolute; display: flex; align-items: center; gap: 10px;
    font-weight: 700; letter-spacing: -1px; line-height: 1;
  }
  .wordmark .mark-dot { width: 18px; height: 18px; border-radius: 50%; background: var(--brand-blue); }
  .card-front .wordmark { left: 36px; top: 34px; font-size: 54px; color: var(--ink); }
  .card-back .wordmark { left: 250px; top: 118px; font-size: 58px; color: var(--paper-text); }

  .person { position: absolute; left: 38px; top: 118px; }
  .person-name { font-weight: 700; font-size: 19px; letter-spacing: .5px; color: var(--ink); text-transform: uppercase; }
  .person-role { font-weight: 400; font-size: 17px; color: var(--ink-soft); margin-top: 2px; }

  .contact-list { position: absolute; left: 38px; top: 190px; list-style: none; }
  .contact-list li {
    display: flex; align-items: center; gap: 10px;
    font-size: 14px; color: var(--ink-soft); margin-bottom: 7px;
  }
  .contact-list svg { width: 12px; height: 12px; fill: var(--ink); flex: none; }

  .address {
    position: absolute; left: 248px; top: 262px; padding-left: 16px;
    border-left: 1px solid #9a9a9a;
    font-size: 13px; line-height: 1.35; color: var(--ink-soft);
  }

  .web-url {
    position: absolute; left: 252px; top: 200px;
    font-size: 13px; letter-spacing: 5px; color: var(--url-grey);
  }
</style>
</head>
<body>
<main class="canvas">

  <section class="card card-front" aria-label="Business card front">
    <svg class="decor" viewBox="0 0 560 320" aria-hidden="true">
      <circle cx="400" cy="150" r="22" fill="var(--dot-light)"/>
      <circle cx="455" cy="172" r="28" fill="var(--dot-light)"/>
      <circle cx="480" cy="240" r="44" fill="var(--dot-light)"/>
      <circle cx="420" cy="330" r="64" fill="var(--dot-light)"/>
    </svg>
    <div class="wordmark"><span class="mark-dot"></span>Bramble</div>
    <div class="person">
      <p class="person-name">Marcus Ellery</p>
      <p class="person-role">Founder/ CEO</p>
    </div>
    <ul class="contact-list">
      <li><svg viewBox="0 0 24 24"><path d="M6.6 10.8a15.1 15.1 0 0 0 6.6 6.6l2.2-2.2a1 1 0 0 1 1-.25 11.4 11.4 0 0 0 3.6.57 1 1 0 0 1 1 1V20a1 1 0 0 1-1 1A17 17 0 0 1 3 4a1 1 0 0 1 1-1h3.5a1 1 0 0 1 1 1c0 1.25.2 2.45.57 3.57a1 1 0 0 1-.25 1z"/></svg>555-214-0387</li>
      <li><svg viewBox="0 0 24 24"><path d="M2 5h20v14H2z M2 5l10 8 10-8" fill="none" stroke="#111" stroke-width="2.4"/></svg>m.ellery@bramble.one</li>
      <li><svg viewBox="0 0 24 24"><circle cx="12" cy="12" r="9" fill="none" stroke="#111" stroke-width="2.4"/><path d="M3 12h18M12 3c3 3 3 15 0 18M12 3c-3 3-3 15 0 18" fill="none" stroke="#111" stroke-width="1.8"/></svg>www.bramble.one</li>
    </ul>
    <address class="address" style="font-style:normal">18 Orchard Lane<br>Fairview, OH 44120</address>
  </section>

  <section class="card card-back" aria-label="Business card back">
    <svg class="decor" viewBox="0 0 560 320" aria-hidden="true">
      <circle cx="110" cy="170" r="95" fill="var(--dot-dark-1)"/>
      <circle cx="290" cy="40" r="60" fill="var(--dot-dark-1)"/>
      <circle cx="420" cy="55" r="36" fill="var(--dot-dark-2)"/>
      <circle cx="500" cy="110" r="28" fill="var(--dot-dark-3)"/>
    </svg>
    <div class="wordmark"><span class="mark-dot"></span>Bramble</div>
    <p class="web-url">www.bramble.one</p>
  </section>

</main>
</body>
</html>
```